*YO!!! Designers Needed!!* Front Page Cover Needed for a $$Billion Dollar$$ Company

We are a manufacturer of aluminum electrolytic capacitors. We are looking to create a front page cover that will be used on our annual report. We are a publicly listed company and work with many Pinnacle 300 companies, so your work will be viewed by the BIG GUNS and EXECUTIVES around the WORLD! If selected, you may be selected for additional work.

The front page cover should be unique. If elegance, modern, bling, and creativity somehow got together and had a child, that's what the cover page would look like!

Inspired Examples attached. Check them out!

www.velmoro.com

Font styles to use
Sans Serif

Requirements
Must have
• 1. Must include the attached logo. Logo size, color, and placement are at your discretion.

2. Should include the text, '2020 Annual Report'

3. The design should incorporate the use of foil and/or be embossed. The foil can be part of the design or can be the full page. See various examples attached for reference.

4. Shall be in A4 size and vertical orientation.
Nice to have
• Feel free to add any icons or stock photos (for example capacitors or circuit boards) if needed.

Be creative here and don't be afraid to be bold! The end product will be printed and budget is not a limiting factor, so feel free to make it extravagant if needed.

Our slogan is "Think Ahead". This slogan can or cannot be part of the theme.

```html
<!DOCTYPE html>
<html lang="en">
<head>
<meta charset="utf-8">
<title>Velmoro 2020 Annual Report Cover</title>
<link href="https://fonts.googleapis.com/css2?family=Rubik+Mono+One&family=Montserrat:wght@500;600&display=swap" rel="stylesheet">
<style>
  :root {
    --page-black: #000000;
    --gold-light: #f3cf6a;
    --gold-mid: #d49a2a;
    --gold-deep: #9a6414;
  }
  html, body {
    margin: 0;
    padding: 0;
    width: 878px;
    height: 1200px;
    overflow: hidden;
    background: var(--page-black);
  }
  .cover {
    position: relative;
    width: 878px;
    height: 1200px;
    background: var(--page-black);
  }
  .cover-art {
    display: block;
    width: 878px;
    height: 1200px;
  }
  .headline {
    font-family: "Rubik Mono One", "Arial Black", sans-serif;
  }
  .brand-name {
    font-family: "Montserrat", Arial, sans-serif;
    font-weight: 600;
  }
  .slogan {
    font-family: "Montserrat", Arial, sans-serif;
    font-weight: 500;
  }
</style>
</head>
<body>
<main class="cover">
  <svg class="cover-art" viewBox="0 0 878 1200" xmlns="http://www.w3.org/2000/svg">
    <defs>
      <linearGradient id="gold-foil" x1="0" y1="0" x2="1" y2="1">
        <stop offset="0" stop-color="var(--gold-deep)"/>
        <stop offset="0.3" stop-color="var(--gold-light)"/>
        <stop offset="0.55" stop-color="var(--gold-mid)"/>
        <stop offset="0.8" stop-color="var(--gold-light)"/>
        <stop offset="1" stop-color="var(--gold-deep)"/>
      </linearGradient>
    </defs>

    <g class="headline" fill="url(#gold-foil)" role="img" aria-label="Gold foil lettering with circuit board traces">
      <text class="headline-year" x="63" y="460" font-size="300" textLength="735" lengthAdjust="spacingAndGlyphs">2020</text>
      <text class="headline-title" x="63" y="618" font-size="140" textLength="745" lengthAdjust="spacingAndGlyphs">ANNUAL</text>
      <text class="headline-title" x="63" y="787" font-size="200" textLength="738" lengthAdjust="spacingAndGlyphs">REPORT</text>
    </g>

    <g class="brand" fill="url(#gold-foil)">
      <text class="brand-name" x="820" y="1112" font-size="84" text-anchor="end" textLength="262" lengthAdjust="spacingAndGlyphs">Velmoro</text>
      <rect class="footer-bar" x="0" y="1134" width="664" height="12"/>
      <rect class="footer-rule" x="664" y="1134" width="156" height="2"/>
      <text class="slogan" x="672" y="1162" font-size="18" textLength="148" lengthAdjust="spacingAndGlyphs">BUILD FORWARD.</text>
    </g>
  </svg>
</main>
</body>
</html>
```